Bref créative
Stationary - Morvane Advisory
Business Card, Letterhead & Pen Design
Professional
Helmut Draven
Director
Address line 1
Address line 2
Address line 3
Address line 4
Post Code
QRP@QRP.example
For the business card I like the idea of front/back designs, where either there is something which joins the front and back or there is a slightly modified logo on the back... You're call, I'm open to anything here, so if you come up with something just try it out, I'll give everyone feedback where possible!
Please don't just stick my logo on a pen and say "hey, here you go...", for the pen design I'm looking for colours etc and where they are placed on the pen too!
Anything you think would look good!
Image file to show the logo
Extra images (inc psds!) for the logo

```html
<!DOCTYPE html>
<html lang="en">
<head>
<meta charset="utf-8">
<title>Morvane Advisory – Business Card</title>
<link href="https://fonts.googleapis.com/css2?family=Arimo:wght@400;700&display=swap" rel="stylesheet">
<style>
  :root {
    --backdrop: #2b2b2b;
    --card: #ffffff;
    --teal: #1a9ec4;
    --teal-light: #5cc6e4;
    --teal-dark: #0e7fa3;
    --rule-grey: #c9ced2;
    --ink: #1e1e1e;
    --ink-soft: #555a5e;
  }
  * { box-sizing: border-box; margin: 0; padding: 0; }
  html, body {
    width: 1200px; height: 780px; overflow: hidden;
    background: var(--backdrop);
    font-family: "Arimo", Arial, sans-serif;
  }
  .canvas {
    width: 1200px; height: 780px;
    display: flex; align-items: center; justify-content: center;
  }
  .business-card {
    position: relative;
    width: 960px; height: 580px;
    background: var(--card);
    border-radius: 40px;
    overflow: hidden;
    box-shadow: 0 18px 40px rgba(0,0,0,0.45);
  }
  .brand {
    position: absolute; top: 110px; left: 0; right: 0;
    display: flex; align-items: center; justify-content: center; gap: 22px;
  }
  .brand-dot {
    width: 70px; height: 70px; border-radius: 50%;
    background: var(--teal);
  }
  .brand-name {
    font-size: 62px; font-weight: 700; color: var(--teal);
    letter-spacing: 1px;
  }
  .name-band {
    position: absolute; left: 0; right: 0; top: 262px; height: 90px;
    background: linear-gradient(to bottom, var(--teal-light) 0%, var(--teal) 45%, var(--teal-dark) 100%);
    border-top: 8px solid var(--rule-grey);
    border-bottom: 3px solid var(--rule-grey);
    display: flex; align-items: center; justify-content: center; gap: 24px;
    color: #fff;
  }
  .person-name { font-size: 28px; font-weight: 700; }
  .divider { width: 2px; height: 34px; background: rgba(255,255,255,0.85); }
  .person-role { font-size: 20px; }
  .address {
    position: absolute; top: 398px; left: 0; right: 0;
    text-align: center; font-size: 21px; color: var(--ink);
  }
  .contacts {
    position: absolute; top: 444px; left: 0; right: 0;
    text-align: center; font-size: 21px; color: var(--ink-soft);
  }
  .contacts .label { color: var(--teal); margin-left: 12px; }
  .contacts .label:first-child { margin-left: 0; }
</style>
</head>
<body>
<main class="canvas">
  <article class="business-card">
    <header class="brand">
      <span class="brand-dot"></span>
      <span class="brand-name">Morvane Advisory</span>
    </header>
    <section class="name-band">
      <span class="person-name">Helmut Draven</span>
      <span class="divider"></span>
      <span class="person-role">Director</span>
    </section>
    <p class="address">Suite 102 Street name, State, Zip 2034,Country</p>
    <p class="contacts">
      <span class="label">P:</span> 07000 555 019
      <span class="label">E:</span> QRP@QRP.example
      <span class="label">W:</span> www.qrp.example
    </p>
  </article>
</main>
</body>
</html>
```